Business cards for broker of real estate brokerage company
Business cards
Business cards for broker of real estate brokerage company - Real Estate
Creative Brief
Professional
Peter Marsh
Broker/Owner
2735 Harlow Lane Mount Dora, FL 32757
petermarsh418@mailbrook.net

```html
<!DOCTYPE html>
<html lang="en">
<head>
<meta charset="utf-8">
<title>Harbor Crest Realty – Business Cards</title>
<link href="https://fonts.googleapis.com/css2?family=Open+Sans:wght@400;600&display=swap" rel="stylesheet">
<style>
  :root {
    --backdrop: #2b2c2e;
    --card: #ffffff;
    --card-shade: #eef0f3;
    --brand-blue: #1f3fa8;
    --brand-deep: #132a7a;
    --brand-light: #3f66d6;
    --swoosh-grey: #9aa1aa;
    --text-grey: #555b63;
  }
  * { box-sizing: border-box; margin: 0; padding: 0; }
  html, body {
    width: 1200px; height: 871px; overflow: hidden;
    background: var(--backdrop);
    font-family: "Open Sans", Arial, sans-serif;
  }
  .stage {
    position: relative; width: 1200px; height: 871px;
    display: flex; align-items: center; justify-content: center; gap: 40px;
  }
  .card {
    position: relative; width: 520px; height: 297px;
    background: linear-gradient(180deg, var(--card) 0%, var(--card-shade) 100%);
    overflow: hidden;
  }
  .brand {
    display: flex; align-items: center; gap: 10px;
    color: var(--brand-blue); font-weight: 600; letter-spacing: 1px;
    text-transform: uppercase;
  }
  .brand-dot {
    width: 26px; height: 26px; border-radius: 50%;
    background: var(--brand-blue); flex: none;
  }
  .card-back .brand {
    position: absolute; left: 50%; top: 50%; transform: translate(-50%, -50%);
    font-size: 26px;
  }
  .card-front .brand {
    position: absolute; right: 34px; top: 118px; font-size: 19px;
  }
  .card-front .brand-dot { width: 22px; height: 22px; }
  .holder { position: absolute; left: 38px; top: 30px; }
  .holder-name { color: var(--brand-blue); font-size: 15px; font-weight: 600; }
  .holder-role { color: var(--text-grey); font-size: 10px; margin-top: 2px; }
  .contacts {
    position: absolute; left: 38px; top: 86px; list-style: none;
    color: var(--text-grey); font-size: 10.5px;
  }
  .contacts li { display: flex; align-items: center; gap: 8px; height: 17px; }
  .contacts svg { width: 10px; height: 10px; fill: var(--brand-blue); flex: none; }
  .swoosh { position: absolute; left: 0; bottom: 0; width: 520px; height: 110px; }
</style>
</head>
<body>
<main class="stage">

  <section class="card card-back" aria-label="Card back">
    <div class="brand"><span class="brand-dot"></span>Harbor Crest Realty</div>
  </section>

  <section class="card card-front" aria-label="Card front">
    <div class="holder">
      <p class="holder-name">Peter Marsh</p>
      <p class="holder-role">Consultant</p>
    </div>

    <ul class="contacts">
      <li><svg viewBox="0 0 10 10"><path d="M2 0h2l1 3-1.5 1a6 6 0 0 0 2.5 2.5L7 5l3 1v2c0 1-1 2-2 2A8 8 0 0 1 0 2C0 1 1 0 2 0z"/></svg>012 555 0147</li>
      <li><svg viewBox="0 0 10 10"><path d="M2 0h2l1 3-1.5 1a6 6 0 0 0 2.5 2.5L7 5l3 1v2c0 1-1 2-2 2A8 8 0 0 1 0 2C0 1 1 0 2 0z"/></svg>012 555 0148</li>
      <li><svg viewBox="0 0 10 10"><rect x="0" y="2" width="10" height="7" rx="1"/></svg>012 555 0149</li>
      <li><svg viewBox="0 0 10 10"><rect x="0" y="2" width="10" height="7" rx="1"/></svg>petermarsh418@mailbrook.net</li>
      <li><svg viewBox="0 0 10 10"><circle cx="5" cy="5" r="5"/></svg>www.harborcrestrealty.com</li>
      <li><svg viewBox="0 0 10 10"><path d="M5 0a3.5 3.5 0 0 1 3.5 3.5C8.5 6 5 10 5 10S1.5 6 1.5 3.5A3.5 3.5 0 0 1 5 0z"/></svg>2735 Harlow Lane Mount Dora, FL 32757</li>
    </ul>

    <div class="brand"><span class="brand-dot"></span>Harbor Crest Realty</div>

    <svg class="swoosh" viewBox="0 0 520 110" preserveAspectRatio="none" aria-hidden="true">
      <defs>
        <linearGradient id="blueBand" x1="0" y1="0" x2="1" y2="0">
          <stop offset="0" stop-color="var(--brand-deep)"/>
          <stop offset="0.55" stop-color="var(--brand-light)"/>
          <stop offset="1" stop-color="var(--brand-blue)"/>
        </linearGradient>
      </defs>
      <path d="M0 60 C150 100 330 20 520 28 L520 44 C330 40 170 108 0 80 Z" fill="var(--swoosh-grey)"/>
      <path d="M0 78 C170 110 330 44 520 42 L520 110 L0 110 Z" fill="url(#blueBand)"/>
    </svg>
  </section>

</main>
</body>
</html>
```